Tembo & Lusani Advocates website

An interactive professional law firm website fully synchronized with social media pages.

Target Market(s)

Corporations and professionals

Industry/Entity Type

Professional Service

Number of Pages Required

5+ page

Font styles to use
Sans Serif

Colors

Designer to choose colors to be used in the design.

```html
<!DOCTYPE html>
<html lang="en">
<head>
<meta charset="utf-8">
<title>Tembo &amp; Lusani Advocates</title>
<link href="https://fonts.googleapis.com/css2?family=Montserrat:wght@600;700;800&family=Open+Sans:wght@400;600;700&display=swap" rel="stylesheet">
<style>
:root{
  --maroon:#8c1c2c;
  --maroon-dark:#6f1220;
  --ink:#1d1d1d;
  --text:#4a4a4a;
  --muted:#777;
  --line:#d6d6d6;
  --grey-bg:#f2f2f2;
  --tile:#e6e6e6;
  --dark:#141414;
  --white:#fff;
}
*{box-sizing:border-box;margin:0;padding:0}
html,body{width:1200px;height:5128px;overflow:hidden}
body{font-family:"Open Sans",Arial,sans-serif;color:var(--text);background:var(--white);position:relative}
.section-title{font-family:"Montserrat",Arial,sans-serif;font-weight:800;font-size:50px;letter-spacing:3px;color:var(--ink);text-align:center}

/* header */
.site-header{height:96px;display:flex;align-items:center;justify-content:space-between;padding:0 96px}
.brand{display:flex;align-items:center;gap:12px;font-family:"Open Sans",Arial,sans-serif;font-weight:600;font-size:20px;color:var(--maroon);line-height:1.1}
.brand-square{width:46px;height:46px;background:var(--maroon)}
.main-nav{display:flex;gap:20px;font-size:14px;color:#333}

/* hero */
.hero{position:absolute;top:96px;left:0;width:1200px;height:598px;background:linear-gradient(180deg,#8ea7b8 0%,#5f7a64 45%,#3f5a3f 100%)}
.hero-content{position:absolute;top:126px;width:100%;text-align:center;color:var(--white)}
.hero h1{font-family:"Montserrat",Arial,sans-serif;font-weight:700;font-size:40px;letter-spacing:2px}
.hero p{font-size:24px;margin-top:18px;font-weight:600}
.hero-btn{display:inline-block;margin-top:48px;border:2px solid var(--white);border-radius:30px;padding:14px 42px;font-size:15px;font-weight:700;letter-spacing:1px}
.hero-dots{position:absolute;top:522px;width:100%;display:flex;justify-content:center;gap:6px}
.hero-dots span{width:11px;height:11px;border-radius:50%;border:1.5px solid var(--white)}
.hero-dots span.active{background:var(--white)}

/* history */
.history{position:absolute;top:780px;left:0;width:1200px;text-align:center}
.history-text{width:1010px;margin:60px auto 0;font-size:13.5px;line-height:1.75;color:var(--text)}
.history-text p+p{margin-top:22px}

/* who */
.who{position:absolute;top:1265px;left:0;width:905px;height:582px;background:var(--maroon);color:var(--white);padding:52px 0 0 96px}
.who h2{font-family:"Montserrat",Arial,sans-serif;font-weight:800;font-size:46px;letter-spacing:2px}
.who p{width:420px;font-size:14px;line-height:1.65;margin-top:18px}
.who h3{display:flex;align-items:center;gap:10px;font-size:26px;font-weight:700;margin-top:22px}
.who h3+p{margin-top:8px}
.who-photo{position:absolute;top:1340px;left:598px;width:602px;height:480px;background:linear-gradient(135deg,#5a5f66,#2c2f35 60%,#1c1e22);border:6px solid var(--white)}

/* approach */
.approach{position:absolute;top:1950px;left:0;width:1200px}
.approach-grid{display:flex;gap:28px;justify-content:center;margin-top:58px}
.value-card{width:320px;height:342px;border:1.5px solid var(--line);text-align:center;padding:36px 30px 0}
.value-card svg{height:70px}
.value-card h3{font-family:"Montserrat",Arial,sans-serif;font-size:20px;font-weight:700;color:var(--ink);margin-top:28px;letter-spacing:1px}
.value-card p{font-size:13.5px;line-height:1.6;margin-top:16px}

/* practice */
.practice{position:absolute;top:2514px;left:0;width:1200px;height:770px;background:var(--grey-bg);padding-top:74px}
.practice-grid{display:flex;gap:20px;justify-content:center;margin-top:50px}
.practice-card{width:322px}
.practice-img{height:232px}
.practice-card h3{font-family:"Montserrat",Arial,sans-serif;font-size:22px;font-weight:700;color:var(--ink);margin-top:40px}
.practice-card p{font-size:13.5px;line-height:1.6;margin-top:14px;height:96px}
.read-more{display:inline-block;margin-top:16px;border:2px solid var(--maroon);border-radius:24px;padding:10px 28px;font-size:14px;font-weight:700;color:var(--ink)}

/* clients */
.clients{position:absolute;top:3350px;left:0;width:1200px;text-align:center}
.client-tabs{margin-top:36px;font-size:17px;color:#333}
.client-tabs .active{color:var(--maroon)}
.client-tabs .sep{margin:0 12px}
.client-grid{display:flex;gap:37px;justify-content:center;margin-top:48px}
.client-tile{width:137px;height:137px;border-radius:10px;display:flex;align-items:center;justify-content:center;font-size:16px;font-weight:700;text-align:center;padding:8px;background:var(--tile);color:var(--ink)}

/* team */
.team{position:absolute;top:3779px;left:0;width:1200px;height:701px;background:#fafafa;padding-top:76px}
.team-row{display:flex;justify-content:center;gap:40px;margin-top:62px}
.member{width:220px;text-align:center}
.member-photo{width:220px;height:220px;border-radius:50%;border:5px solid #ddd;background:radial-gradient(circle at 50% 40%,#6b6f78,#2b2d33)}
.member h3{font-size:20px;font-weight:600;color:#333;margin-top:38px;white-space:nowrap}
.member .role{font-size:14px;color:var(--muted);margin-top:6px}
.member-links{display:flex;justify-content:center;gap:10px;margin-top:30px}
.member-links span{width:34px;height:34px;border-radius:50%;border:1.5px solid var(--maroon);display:flex;align-items:center;justify-content:center}
.slider-arrow{position:absolute;top:398px;width:34px;height:34px;border-radius:50%;border:1.5px solid #999;display:flex;align-items:center;justify-content:center}

/* contact */
.contact{position:absolute;top:4480px;left:0;width:1200px;height:648px;background:var(--dark);color:var(--white);padding-top:100px}
.contact .section-title{color:var(--white)}
.contact-cols{display:flex;justify-content:space-between;padding:0 96px;margin-top:72px}
.contact-form{width:630px}
.contact-form h3,.contact-info h3{font-size:22px;font-weight:400}
.field-row{display:flex;gap:30px;margin-top:22px}
.field{border:1px solid #555;height:34px;font-size:13px;color:#bbb;padding:8px 12px;flex:1}
.field.full{margin-top:14px}
.field.message{height:80px}
.submit{display:block;margin:16px 0 0 auto;width:96px;height:34px;border-radius:18px;background:var(--maroon);color:var(--white);font-size:13px;font-weight:700;text-align:center;line-height:34px}
.contact-info{width:330px}
.info-item{display:flex;gap:22px;margin-top:22px;font-size:13px;line-height:1.55;color:#ddd}
.info-icon{flex:none;width:34px;height:34px;border-radius:50%;background:#2a2a2a;display:flex;align-items:center;justify-content:center}
.site-footer{position:absolute;bottom:0;left:0;width:1200px;height:70px;display:flex;align-items:center;justify-content:space-between;padding:0 96px;font-size:12px;color:#ccc}
.social{display:flex;gap:10px}
.social span{width:30px;height:30px;border-radius:50%;background:var(--maroon)}
</style>
</head>
<body>

<header class="site-header">
  <div class="brand"><span class="brand-square"></span><span>Tembo &amp; Lusani<br>Advocates</span></div>
  <nav class="main-nav"><span>History</span><span>Who We Are</span><span>How We Do It</span><span>Practice Areas</span><span>Clients</span><span>Professionals</span><span>Contact Us</span></nav>
</header>

<section class="hero" role="img" aria-label="Aerial photograph of a green city skyline">
  <div class="hero-content">
    <h1>TEMBO &amp; LUSANI ADVOCATES</h1>
    <p>Construction Law | Arbitration | Litigation</p>
    <span class="hero-btn">GET MORE INFO</span>
  </div>
  <div class="hero-dots"><span class="active"></span><span></span><span></span><span></span></div>
</section>

<section class="history">
  <h2 class="section-title">OUR HISTORY</h2>
  <div class="history-text">
    <p>In 1996, our firm was founded and is comprised of 5 Partners and over 15 Associates and support staff fully engaged and focused on client service. The firm is fully auto mated and is run on the latest practice management software with efficient client.</p>
    <p>Focused delivery systems and improved turn around times. Over the years, the firm has worked with the international firm of Harrow Whitfield in successfully representing Harbor Relief Trust against a multimillion dollar law suit and has acted for both local and international corporations from Chinese, Italy, Turkey, South Africa, Zambia and the United Kingdom to build their businesses.</p>
    <p>With over 21 years' experience and having achieved tremendous success for our clients having won over 200 commercial disputes, we are now a specialist firm in Commercial Litigation, Construction Law and Arbitration. We have successfully represented clients in ground breaking cases in the financial services sector that we are the firm of choice in banking and insurance litigation.</p>
  </div>
</section>

<section class="who">
  <h2>WHO WE ARE</h2>
  <p>Tembo &amp; Lusani Advocates are a specialist commercial law firm in Uganda focusing on commercial litigation, construction law and arbitration.</p>
  <h3><svg width="24" height="18" viewBox="0 0 24 18"><path d="M1 9C5 2 19 2 23 9C19 16 5 16 1 9Z" fill="#fff"/><circle cx="12" cy="9" r="4" fill="#8c1c2c"/></svg>Vision</h3>
  <p>To be the firm of choice in our niche practice areas of commercial law.</p>
  <h3><svg width="22" height="22" viewBox="0 0 22 22"><circle cx="11" cy="11" r="10" fill="#fff"/><circle cx="11" cy="11" r="6" fill="#8c1c2c"/><circle cx="11" cy="11" r="2.5" fill="#fff"/></svg>Mission</h3>
  <p>To provide legal services focused on commercial litigation, construction law and arbitration with efficiency, integrity and client satisfaction.</p>
</section>
<div class="who-photo" role="img" aria-label="Group photograph of the firm's partners and associates in business suits"></div>

<section class="approach">
  <h2 class="section-title">HOW WE DO IT</h2>
  <div class="approach-grid">
    <div class="value-card">
      <svg viewBox="0 0 70 70" width="70"><path d="M8 24H58M48 14L60 24L48 34M62 46H12M22 36L10 46L22 56" stroke="#8c1c2c" stroke-width="6" fill="none"/></svg>
      <h3>INTEGRITY</h3>
      <p>We maintain ethical behaviour and strict moral values. We are honest and trustworthy in our dealings with each other, with our clients and with all others with whom we deal.</p>
    </div>
    <div class="value-card">
      <svg viewBox="0 0 80 70" width="80"><g fill="#8c1c2c"><circle cx="40" cy="18" r="10"/><path d="M24 52C24 38 56 38 56 52Z"/><circle cx="16" cy="28" r="7"/><path d="M4 56C4 44 26 44 26 56Z"/><circle cx="64" cy="28" r="7"/><path d="M54 56C54 44 76 44 76 56Z"/></g></svg>
      <h3>PARTNERSHIP</h3>
      <p>We partner with our clients and keep a close and interactive relationship that enriches our business knowledge and allows us to provide strategic, innovative and forward-thinking solutions fit to meet the challenges they face every day.</p>
    </div>
    <div class="value-card">
      <svg viewBox="0 0 80 70" width="80"><g fill="none" stroke="#8c1c2c"><circle cx="30" cy="38" r="14" stroke-width="10" stroke-dasharray="6 5"/><circle cx="30" cy="38" r="6" stroke-width="4"/><circle cx="60" cy="18" r="9" stroke-width="7" stroke-dasharray="4 4"/></g></svg>
      <h3>EFFICIENCY</h3>
      <p>We work to surpass our clients' expectations. We are practical and solution driven in our approach. We are innovative and creative, and we focus sharply and firmly on the issues we undertake.</p>
    </div>
  </div>
</section>

<section class="practice">
  <h2 class="section-title">PRACTICE AREAS</h2>
  <div class="practice-grid">
    <article class="practice-card">
      <div class="practice-img" role="img" aria-label="Construction cranes against a sunset sky" style="background:linear-gradient(180deg,#3a6fb0,#e0953a 70%,#5a3a1e)"></div>
      <h3>CONSTRUCTION LAW</h3>
      <p>Our Construction Law department is headed by our Senior Partner Samuel Lusani, who is highly qualified and experienced in Construction law and in providing advice...</p>
      <span class="read-more">READ MORE</span>
    </article>
    <article class="practice-card">
      <div class="practice-img" role="img" aria-label="Hands signing a contract document" style="background:linear-gradient(135deg,#c9894a,#f1d7b4 55%,#8a5a32)"></div>
      <h3>COMMERCIAL LITIGATION</h3>
      <p>We have a reputation for producing excellent results for our litigation clients. Since 1996, the firm has an excellent track record in winning for our clients in commercial disputes.</p>
      <span class="read-more">READ MORE</span>
    </article>
    <article class="practice-card">
      <div class="practice-img" role="img" aria-label="Paper notice about an arbitration hearing beside a pen" style="background:linear-gradient(135deg,#dfe3e8,#b9c2cc)"></div>
      <h3>ARBITRATION</h3>
      <p>We advise clients on both domestic and international arbitration proceedings and other forms of intermediate and alternative dispute resolution, as well as on contract...</p>
      <span class="read-more">READ MORE</span>
    </article>
  </div>
</section>

<section class="clients">
  <h2 class="section-title">OUR CLIENTS</h2>
  <div class="client-tabs"><span class="active">Commercial Litigation and Transactions</span><span class="sep">|</span>Construction &amp; Arbitration<span class="sep">|</span>Corporate Advisory</div>
  <div class="client-grid">
    <div class="client-tile">Swiftlane</div>
    <div class="client-tile">Oakfield Foods</div>
    <div class="client-tile">Keystone Group</div>
    <div class="client-tile">Meridian Insure</div>
    <div class="client-tile">Boxwell</div>
    <div class="client-tile">Autocare Hub</div>
  </div>
</section>

<section class="team">
  <h2 class="section-title">OUR PROFESSIONALS</h2>
  <span class="slider-arrow" style="left:32px"><svg width="10" height="12" viewBox="0 0 10 12"><path d="M8 1L2 6L8 11" stroke="#777" stroke-width="2" fill="none"/></svg></span>
  <span class="slider-arrow" style="right:32px"><svg width="10" height="12" viewBox="0 0 10 12"><path d="M2 1L8 6L2 11" stroke="#777" stroke-width="2" fill="none"/></svg></span>
  <div class="team-row">
    <div class="member"><div class="member-photo" role="img" aria-label="Portrait of the managing partner"></div><h3>PETER M. TEMBO</h3><p class="role">Managing Partner</p><div class="member-links"><span><svg width="14" height="10" viewBox="0 0 14 10"><rect x="0.5" y="0.5" width="13" height="9" fill="#8c1c2c"/><path d="M1 1L7 6L13 1" stroke="#fff" fill="none"/></svg></span><span><svg width="14" height="14" viewBox="0 0 14 14"><path d="M3 1L5 4L4 6C5 8 6 9 8 10L10 9L13 11L11 13C6 13 1 8 1 3Z" fill="#8c1c2c"/></svg></span></div></div>
    <div class="member"><div class="member-photo" role="img" aria-label="Portrait of the senior partner"></div><h3>SAMUEL R. LUSANI</h3><p class="role">Senior Partner</p><div class="member-links"><span><svg width="14" height="10" viewBox="0 0 14 10"><rect x="0.5" y="0.5" width="13" height="9" fill="#8c1c2c"/><path d="M1 1L7 6L13 1" stroke="#fff" fill="none"/></svg></span><span><svg width="14" height="14" viewBox="0 0 14 14"><path d="M3 1L5 4L4 6C5 8 6 9 8 10L10 9L13 11L11 13C6 13 1 8 1 3Z" fill="#8c1c2c"/></svg></span></div></div>
    <div class="member"><div class="member-photo" role="img" aria-label="Portrait of the head of litigation"></div><h3>ISAAC MUTEBI</h3><p class="role">Head of Litigation</p><div class="member-links"><span><svg width="14" height="10" viewBox="0 0 14 10"><rect x="0.5" y="0.5" width="13" height="9" fill="#8c1c2c"/><path d="M1 1L7 6L13 1" stroke="#fff" fill="none"/></svg></span><span><svg width="14" height="14" viewBox="0 0 14 14"><path d="M3 1L5 4L4 6C5 8 6 9 8 10L10 9L13 11L11 13C6 13 1 8 1 3Z" fill="#8c1c2c"/></svg></span></div></div>
    <div class="member"><div class="member-photo" role="img" aria-label="Portrait of the head of business development"></div><h3>Daniel Nkurunziza</h3><p class="role">Head of Business Development</p><div class="member-links"><span><svg width="14" height="10" viewBox="0 0 14 10"><rect x="0.5" y="0.5" width="13" height="9" fill="#8c1c2c"/><path d="M1 1L7 6L13 1" stroke="#fff" fill="none"/></svg></span><span><svg width="14" height="14" viewBox="0 0 14 14"><path d="M3 1L5 4L4 6C5 8 6 9 8 10L10 9L13 11L11 13C6 13 1 8 1 3Z" fill="#8c1c2c"/></svg></span></div></div>
  </div>
</section>

<section class="contact">
  <h2 class="section-title">CONTACT US</h2>
  <div class="contact-cols">
    <div class="contact-form">
      <h3>CONTACT FORM</h3>
      <div class="field-row"><div class="field">Name :</div><div class="field">Phone no :</div></div>
      <div class="field full">Email :</div>
      <div class="field full message">Message :</div>
      <span class="submit">SUBMIT</span>
    </div>
    <div class="contact-info">
      <h3>CONTACT INFORMATION</h3>
      <div class="info-item"><span class="info-icon"><svg width="12" height="16" viewBox="0 0 12 16"><path d="M6 0C2.7 0 0 2.6 0 6C0 10 6 16 6 16C6 16 12 10 12 6C12 2.6 9.3 0 6 0Z" fill="#fff"/><circle cx="6" cy="6" r="2.2" fill="#2a2a2a"/></svg></span><span>Head Office Address &amp; Contacts<br>Plot 14, Riverside Avenue<br>2nd Floor, Crest House<br>P. O Box 4410<br>Kampala, Uganda</span></div>
      <div class="info-item"><span class="info-icon"><svg width="14" height="14" viewBox="0 0 14 14"><path d="M3 1L5 4L4 6C5 8 6 9 8 10L10 9L13 11L11 13C6 13 1 8 1 3Z" fill="#fff"/></svg></span><span style="padding-top:8px">0414 555 210</span></div>
      <div class="info-item"><span class="info-icon"><svg width="10" height="15" viewBox="0 0 10 15"><rect x="0.5" y="0.5" width="9" height="14" rx="1.5" fill="#fff"/><rect x="2" y="2" width="6" height="9" fill="#2a2a2a"/></svg></span><span style="padding-top:8px">+256 (0) 700 555 318</span></div>
      <div class="info-item"><span class="info-icon"><svg width="14" height="10" viewBox="0 0 14 10"><rect x="0.5" y="0.5" width="13" height="9" fill="#fff"/><path d="M1 1L7 6L13 1" stroke="#2a2a2a" fill="none"/></svg></span><span style="padding-top:8px">info@tembolusani.com</span></div>
    </div>
  </div>
  <footer class="site-footer">
    <span>Copyright © 2018, Tembo &amp; Lusani Advocates. All rights reserved. Privacy Policy | Terms and Conditions.</span>
    <div class="social"><span></span><span></span><span></span><span></span></div>
  </footer>
</section>

</body>
</html>
```